Tending Our Garden eBook Cover Design

I want to deisgn a cover for my eBook (FRONT COVER) and the title is:

Under the Willow Tree; Where I Found My Quiet Strength and Where You Might Too
By KT Dorran

TITLE CHANGED TO: UNDER THE WILLOW TREE; WHERE I FOUND MY QUIET STRENGTH AND WHERE YOU MIGHT TOO

The color palette is attached. Along with some photos options of me. Along with the ebook in WORD Document. My website is www.KTDorranLive.example. You can use a different color palette if you think it is best

Target Market(s)

women who look to build a personal brand

Industry/Entity Type

health and wellness

Requirements
Must have
• the title
Nice to have
• use my picture on the cover; but that is optional
Should not have
• any men

```html
<!DOCTYPE html>
<html lang="en">
<head>
<meta charset="utf-8">
<title>Under the Willow Tree — KT Dorran</title>
<link href="https://fonts.googleapis.com/css2?family=Anton&family=Yellowtail&family=Open+Sans:ital,wght@1,600&display=swap" rel="stylesheet">
<style>
  :root {
    --backdrop: #cf9da7;
    --cover-rose: #bd7788;
    --cover-glow: #e4b6c4;
    --band-maroon: #7e414b;
    --strip-white: #ececec;
    --title-white: #efefef;
    --frame-white: #f6f6f6;
    --photo-red: #d8241c;
    --photo-deep: #8a2c35;
  }
  * { margin: 0; padding: 0; box-sizing: border-box; }
  html, body {
    width: 1200px; height: 1125px; overflow: hidden;
    background: var(--backdrop);
  }
  .cover {
    position: absolute; left: 250px; top: 25px;
    width: 700px; height: 1075px;
    background: radial-gradient(circle at 55% 38%, var(--cover-glow) 0%, var(--cover-rose) 62%);
    overflow: hidden;
  }
  .cover-frame {
    position: absolute; left: 20px; top: 30px; right: 20px; height: 760px;
    border: 4px solid var(--frame-white); border-bottom: none;
  }
  .title {
    position: absolute; right: 44px; top: 50px;
    text-align: right;
    font-family: "Anton", "Impact", sans-serif;
    font-weight: 400;
    color: var(--title-white);
    line-height: 1.02;
    text-shadow: 2px 3px 4px rgba(70, 25, 35, 0.45);
    text-transform: uppercase;
    white-space: nowrap;
  }
  .title span { display: block; }
  .title .l1 { font-size: 104px; }
  .title .l2 { font-size: 86px; }
  .title .l3 { font-size: 78px; }
  .title .l4 { font-size: 66px; }
  .title .l5 { font-size: 66px; }
  .title .l6 { font-size: 56px; }
  .title .l7 { font-size: 56px; }
  .title .l8 { font-size: 104px; }
  .author-photo {
    position: absolute; left: 40px; top: 330px;
    width: 330px; height: 460px;
  }
  .author-band {
    position: absolute; left: 0; top: 790px; width: 100%; height: 210px;
    background: var(--band-maroon);
  }
  .author-box {
    position: absolute; left: 145px; top: 35px; width: 410px; height: 150px;
    border: 2px dashed var(--frame-white);
    display: flex; align-items: center; justify-content: center;
  }
  .author-name {
    font-family: "Yellowtail", cursive;
    font-size: 76px; color: var(--frame-white);
  }
  .web-strip {
    position: absolute; left: 0; top: 1000px; width: 100%; height: 38px;
    background: var(--strip-white);
    display: flex; align-items: center; justify-content: center;
  }
  .web-address {
    font-family: "Open Sans", sans-serif; font-style: italic; font-weight: 600;
    font-size: 23px; color: var(--band-maroon);
  }
  .cover-foot {
    position: absolute; left: 0; top: 1038px; width: 100%; height: 37px;
    background: var(--band-maroon);
  }
</style>
</head>
<body>
  <main class="cover">
    <div class="cover-frame"></div>

    <svg class="author-photo" viewBox="0 0 330 460" role="img" aria-label="Photo of the author in a red dress seated in a director's chair">
      <defs>
        <linearGradient id="photoTone" x1="0" y1="0" x2="0" y2="1">
          <stop offset="0" stop-color="#bf7f8d" stop-opacity="0"/>
          <stop offset="0.35" stop-color="#8a2c35" stop-opacity="0.55"/>
          <stop offset="1" stop-color="#d8241c"/>
        </linearGradient>
      </defs>
      <rect width="330" height="460" fill="url(#photoTone)"/>
    </svg>

    <h1 class="title">
      <span class="l1">Under the</span>
      <span class="l2">Willow Tree;</span>
      <span class="l3">Where I Found</span>
      <span class="l4">My Quiet</span>
      <span class="l5">Strength</span>
      <span class="l6">And Where</span>
      <span class="l7">You Might</span>
      <span class="l8">Too</span>
    </h1>

    <section class="author-band">
      <div class="author-box">
        <p class="author-name">KT Dorran</p>
      </div>
    </section>

    <div class="web-strip">
      <p class="web-address">www.KTDorranLive.example</p>
    </div>
    <div class="cover-foot"></div>
  </main>
</body>
</html>
```